TLA marine wildlife conservation strategy

The Coastal Habitat Alliance (tla-reefs.org) needs an illustration to explain in a captivating and clear fashion the influences and interactions underlying our marine wildlife conservation planning and policymaking process. This will be included in our forthcoming strategy paper, and widely presented in conferences. Ultimately, this illustration will help governments take the right decisions to protect wildlife and natural resources.
Guidelines:
Size: The illustration shall fit in a A4 page, and also render nicely on a projector screen (1920x1080)
Colors: Avoid too colorful and 'playful' color code
Text: - Case shall be consistent throughout the graphic (unlike the draft design provided)
Graphic elements:
- In the top right of the graphic there is supposed to be a map of Myanmar. The map is attached. Feel free to adjust the map colors and style to match the illustration.
The only key areas we shall include in the map are:
- Myanmar borders
- EEZ (green),
- state/region borders (dotted lines),
- two marine corridors (blue and light red).
Everything else shall be left out (such as minimap, legend, scale, compass, SEZ).
- On the bottom right, it's important for the national benefits to be presented as a Venn diagram like in the original draft illustration (three intersecting circles)
Any questions? Please ask: dmarsh@tla-reefs.org
Thank you!
Target Market(s)
Scientists, policy makers.
Industry/Entity Type
Environment

```html
<!DOCTYPE html>
<html lang="en">
<head>
<meta charset="utf-8">
<title>TLA Marine Spatial Planning Strategy</title>
<link rel="stylesheet" href="https://fonts.googleapis.com/css2?family=Roboto+Condensed:wght@400;700&family=Roboto:wght@400;700&display=swap">
<style>
  :root {
    --stage: #2a2a2c;
    --sea-light: #a6ecfb;
    --sea-mid: #3d9be0;
    --sea-deep: #1a4fa3;
    --leaf: #7ba77b;
    --leaf-dark: #5d8a62;
    --leaf-line: #d9ead3;
    --hex: #5cb2ec;
    --ink: #14213a;
    --grey: #bfc2c6;
    --grey-dark: #9ea3a8;
    --rust: #cd6a2c;
    --rust-dark: #b5531e;
    --moss: #6d9870;
    --arrow-blue: #5bb5ef;
    --white: #ffffff;
  }
  html, body {
    margin: 0;
    padding: 0;
    width: 1200px;
    height: 953px;
    overflow: hidden;
    background: var(--stage);
  }
  .poster {
    position: absolute;
    left: 0;
    top: 52px;
    width: 1200px;
    height: 848px;
    display: block;
  }
  .headline { font-family: "Roboto Condensed", sans-serif; font-weight: 700; fill: var(--white); font-size: 25px; }
  .title { font-family: "Roboto Condensed", sans-serif; font-weight: 700; fill: #0b0f1a; font-size: 28px; }
  .hex-label { font-family: "Roboto", sans-serif; font-size: 13px; fill: var(--ink); }
  .ring-title { font-family: "Roboto Condensed", sans-serif; font-weight: 700; font-size: 27px; fill: var(--white); letter-spacing: 1px; }
  .ring-title.dark { fill: #0f1a2b; }
  .stakeholder { font-family: "Roboto Condensed", sans-serif; font-size: 15px; fill: #111; letter-spacing: 1px; }
  .flow-label { font-family: "Roboto Condensed", sans-serif; font-weight: 700; font-size: 17px; fill: #0c1b3a; letter-spacing: 1px; }
  .core-label { font-family: "Roboto Condensed", sans-serif; font-weight: 700; font-size: 25px; fill: #111; }
  .benefits-title { font-family: "Roboto Condensed", sans-serif; font-weight: 700; font-size: 38px; fill: #0b1530; letter-spacing: 1px; }
  .venn-label { font-family: "Roboto", sans-serif; font-weight: 700; font-size: 13px; fill: #111; }
  .cycle-label { font-family: "Roboto Condensed", sans-serif; font-size: 15px; fill: #111; letter-spacing: 1px; }
  .planning-wheel { filter: drop-shadow(0 6px 10px rgba(0,0,0,.35)); }
  .leaf-box { filter: drop-shadow(0 4px 6px rgba(0,0,0,.3)); }
</style>
</head>
<body>
<svg class="poster" viewBox="0 0 1412 998" xmlns="http://www.w3.org/2000/svg">
  <defs>
    <radialGradient id="sea" cx="0.5" cy="0.12" r="0.95">
      <stop offset="0" stop-color="var(--sea-light)"/>
      <stop offset="0.35" stop-color="var(--sea-mid)"/>
      <stop offset="1" stop-color="var(--sea-deep)"/>
    </radialGradient>
    <linearGradient id="leafFill" x1="0" y1="0" x2="0" y2="1">
      <stop offset="0" stop-color="#98c08f"/>
      <stop offset="1" stop-color="var(--leaf-dark)"/>
    </linearGradient>
    <linearGradient id="mapFill" x1="0" y1="0" x2="0" y2="1">
      <stop offset="0" stop-color="#f4f5f6"/>
      <stop offset="1" stop-color="#c9ccd0"/>
    </linearGradient>
    <radialGradient id="coreFill" cx="0.45" cy="0.4" r="0.7">
      <stop offset="0" stop-color="#f1f2f4"/>
      <stop offset="1" stop-color="#b9bdc3"/>
    </radialGradient>
    <marker id="whiteHead" markerUnits="userSpaceOnUse" markerWidth="34" markerHeight="34" refX="8" refY="17" orient="auto">
      <path d="M0,2 L32,17 L0,32 Z" fill="var(--white)" stroke="#333" stroke-width="1.5"/>
    </marker>
    <marker id="blueHead" markerUnits="userSpaceOnUse" markerWidth="40" markerHeight="60" refX="4" refY="30" orient="auto">
      <path d="M0,0 L36,30 L0,60 Z" fill="var(--arrow-blue)"/>
    </marker>
    <clipPath id="clipEcon"><circle cx="1213" cy="661" r="100"/></clipPath>
    <clipPath id="clipSocial"><circle cx="1130" cy="773" r="100"/></clipPath>

    <path id="arcConsensus" d="M509.6,293.2 A272 272 0 0 1 980.7,538.4"/>
    <path id="arcCapacity" d="M535.7,315 A238 238 0 0 1 947.9,529.6"/>
    <path id="arcData" d="M672,729 A265 265 0 0 1 547.7,265"/>
    <path id="arcInstitutional" d="M989,444.3 A272 272 0 0 1 625,723.6"/>
    <path id="arcArrangements" d="M953.1,447.4 A236 236 0 0 1 637.3,689.8"/>
    <path id="arcStakeTop" d="M611.9,341.6 A165 165 0 0 1 882.4,482.4"/>
    <path id="arcStakeRight" d="M882.4,482.4 A165 165 0 0 1 689.3,630.5"/>
    <path id="arcStakeLeft" d="M689.3,630.5 A165 165 0 0 1 611.9,341.6"/>
    <path id="arcVision" d="M631.2,407.2 A106 106 0 0 1 793,393"/>
    <path id="arcCoordination" d="M814.1,423.2 A106 106 0 0 1 745.4,570.4"/>
    <path id="arcDecision" d="M708.8,573.6 A106 106 0 0 1 615.6,440.6"/>
    <path id="arcBenefits" d="M1005,775 Q1030,560 1250,540"/>
    <path id="arcAdaptive" d="M1140,330 Q1080,300 1025,335"/>
    <path id="arcManagement" d="M1020,405 Q1075,440 1140,415"/>
  </defs>

  <rect class="sea" width="1412" height="998" fill="url(#sea)"/>

  <!-- Headline -->
  <text class="title" x="1392" y="41" text-anchor="end">SPATIAL MANAGEMENT PLAN</text>

  <!-- Map area -->
  <rect class="map" role="img" aria-label="Map of Myanmar showing national borders, EEZ, state and region borders and two marine corridors"
        x="1130" y="48" width="265" height="460" rx="40" fill="url(#mapFill)" opacity="0.92"/>

  <!-- Pressure boxes -->
  <g class="leaf-box pressure-political">
    <path d="M287,18 H513 Q558,18 558,63 V134 Q558,148 544,148 H318 Q273,148 273,103 V32 Q273,18 287,18Z" fill="url(#leafFill)"/>
    <path d="M289,26 H512 Q550,26 550,64 V132 Q550,140 542,140 H319 Q281,140 281,102 V34 Q281,26 289,26Z" fill="none" stroke="var(--leaf-line)" stroke-width="1.2"/>
    <text class="headline" x="411" y="90" text-anchor="middle">POLITICAL TRANSITION</text>
  </g>

  <g class="leaf-box pressure-growth">
    <path d="M37,181 H335 Q395,181 395,241 V354 Q395,368 381,368 H83 Q23,368 23,308 V195 Q23,181 37,181Z" fill="url(#leafFill)"/>
    <path d="M39,189 H335 Q387,189 387,241 V352 Q387,360 379,360 H83 Q31,360 31,308 V197 Q31,189 39,189Z" fill="none" stroke="var(--leaf-line)" stroke-width="1.2"/>
    <text class="headline" text-anchor="middle">
      <tspan x="202" y="259">INCREASING DEVELOPMENTAL</tspan>
      <tspan x="202" y="291">PRESSURES FROM RAPID</tspan>
      <tspan x="202" y="323">ECONOMIC GROWTH</tspan>
    </text>
  </g>

  <g class="leaf-box pressure-coordination">
    <path d="M46,388 H283 Q353,388 353,458 V949 Q353,963 339,963 H102 Q32,963 32,893 V402 Q32,388 46,388Z" fill="url(#leafFill)"/>
    <path d="M48,396 H283 Q345,396 345,458 V947 Q345,955 337,955 H102 Q40,955 40,893 V404 Q40,396 48,396Z" fill="none" stroke="var(--leaf-line)" stroke-width="1.2"/>
    <text class="headline" text-anchor="middle" style="font-size:21px">
      <tspan x="187" y="441">WEAK COORDINATION</tspan>
      <tspan x="187" y="469">BETWEEN MARINE</tspan>
      <tspan x="187" y="497">SECTORS</tspan>
    </text>
    <g class="sector-hex" transform="translate(129,566)">
      <polygon points="0,-62 53.7,-31 53.7,31 0,62 -53.7,31 -53.7,-31" fill="var(--hex)"/>
      <polygon points="0,-54 46.8,-27 46.8,27 0,54 -46.8,27 -46.8,-27" fill="none" stroke="#fff" stroke-width="1.2" stroke-dasharray="5 4"/>
      <text class="hex-label" text-anchor="middle"><tspan x="0" y="-3">Coastal</tspan><tspan x="0" y="13">Tourism</tspan></text>
    </g>
    <g class="sector-hex" transform="translate(257,568)">
      <polygon points="0,-62 53.7,-31 53.7,31 0,62 -53.7,31 -53.7,-31" fill="var(--hex)"/>
      <polygon points="0,-54 46.8,-27 46.8,27 0,54 -46.8,27 -46.8,-27" fill="none" stroke="#fff" stroke-width="1.2" stroke-dasharray="5 4"/>
      <text class="hex-label" text-anchor="middle"><tspan x="0" y="-11">Marine and</tspan><tspan x="0" y="5">Coastal</tspan><tspan x="0" y="21">Conservation</tspan></text>
    </g>
    <g class="sector-hex" transform="translate(190,670)">
      <polygon points="0,-62 53.7,-31 53.7,31 0,62 -53.7,31 -53.7,-31" fill="var(--hex)"/>
      <polygon points="0,-54 46.8,-27 46.8,27 0,54 -46.8,27 -46.8,-27" fill="none" stroke="#fff" stroke-width="1.2" stroke-dasharray="5 4"/>
      <text class="hex-label" text-anchor="middle"><tspan x="0" y="-11">Navy and</tspan><tspan x="0" y="5">Marine</tspan><tspan x="0" y="21">Police</tspan></text>
    </g>
    <g class="sector-hex" transform="translate(123,772)">
      <polygon points="0,-62 53.7,-31 53.7,31 0,62 -53.7,31 -53.7,-31" fill="var(--hex)"/>
      <polygon points="0,-54 46.8,-27 46.8,27 0,54 -46.8,27 -46.8,-27" fill="none" stroke="#fff" stroke-width="1.2" stroke-dasharray="5 4"/>
      <text class="hex-label" text-anchor="middle"><tspan x="0" y="-3">Marine</tspan><tspan x="0" y="13">Fisheries</tspan></text>
    </g>
    <g class="sector-hex" transform="translate(255,774)">
      <polygon points="0,-62 53.7,-31 53.7,31 0,62 -53.7,31 -53.7,-31" fill="var(--hex)"/>
      <polygon points="0,-54 46.8,-27 46.8,27 0,54 -46.8,27 -46.8,-27" fill="none" stroke="#fff" stroke-width="1.2" stroke-dasharray="5 4"/>
      <text class="hex-label" text-anchor="middle"><tspan x="0" y="-11">Offshore Gas</tspan><tspan x="0" y="5">Exploration and</tspan><tspan x="0" y="21">Production</tspan></text>
    </g>
    <g class="sector-hex" transform="translate(187,878)">
      <polygon points="0,-62 53.7,-31 53.7,31 0,62 -53.7,31 -53.7,-31" fill="var(--hex)"/>
      <polygon points="0,-54 46.8,-27 46.8,27 0,54 -46.8,27 -46.8,-27" fill="none" stroke="#fff" stroke-width="1.2" stroke-dasharray="5 4"/>
      <text class="hex-label" text-anchor="middle"><tspan x="0" y="-3">Maritime</tspan><tspan x="0" y="13">Transport</tspan></text>
    </g>
  </g>

  <g class="leaf-box pressure-ecosystems">
    <path d="M405,778 H701 Q761,778 761,838 V949 Q761,963 747,963 H451 Q391,963 391,903 V792 Q391,778 405,778Z" fill="url(#leafFill)"/>
    <path d="M407,786 H701 Q753,786 753,838 V947 Q753,955 745,955 H451 Q399,955 399,903 V794 Q399,786 407,786Z" fill="none" stroke="var(--leaf-line)" stroke-width="1.2"/>
    <text class="headline" text-anchor="middle">
      <tspan x="575" y="850">DECLINING MARINE AND</tspan>
      <tspan x="575" y="883">COASTAL ECOSYSTEMS AND</tspan>
      <tspan x="575" y="915">RESOURCES</tspan>
    </text>
  </g>

  <!-- Input arrows -->
  <g class="input-arrows" fill="none" stroke="var(--white)" stroke-width="9" stroke-linecap="round">
    <path d="M565,80 Q655,70 690,115" marker-end="url(#whiteHead)"/>
    <path d="M387,228 Q440,185 500,198" marker-end="url(#whiteHead)"/>
    <path d="M365,660 Q410,660 425,620" marker-end="url(#whiteHead)"/>
    <path d="M447,766 Q475,728 545,732" marker-end="url(#whiteHead)"/>
  </g>

  <!-- Planning wheel -->
  <g class="planning-wheel">
    <circle cx="718" cy="474" r="314" fill="var(--rust-dark)"/>
    <path class="segment-consensus" d="M517.4,229 A312 312 0 0 1 1028.8,495.2 L847.5,479.3 A130 130 0 0 0 634.4,368.4 Z" fill="var(--grey)"/>
    <path class="segment-institutional" d="M1028.8,495.2 A312 312 0 0 1 663.8,775.3 L695.4,596 A130 130 0 0 0 847.5,479.3 Z" fill="var(--moss)"/>
    <path class="segment-data" d="M663.8,775.3 A312 312 0 0 1 517.4,229 L634.4,368.4 A130 130 0 0 0 695.4,596 Z" fill="var(--rust)"/>
    <circle cx="718" cy="468" r="205" fill="none" stroke="rgba(0,0,0,.12)" stroke-width="2"/>
  </g>

  <text class="ring-title"><textPath href="#arcConsensus" startOffset="50%" text-anchor="middle">CONSENSUS BUILDING</textPath></text>
  <text class="ring-title"><textPath href="#arcCapacity" startOffset="50%" text-anchor="middle">AND CAPACITY DEVELOPMENT</textPath></text>
  <text class="ring-title"><textPath href="#arcData" startOffset="50%" text-anchor="middle">DATA KNOWLEDGE STENGTHENING</textPath></text>
  <text class="ring-title"><textPath href="#arcInstitutional" startOffset="50%" text-anchor="middle">INSTITUTIONAL DEVELOPMENT OF</textPath></text>
  <text class="ring-title"><textPath href="#arcArrangements" startOffset="50%" text-anchor="middle">ARRANGEMENTS</textPath></text>

  <text class="stakeholder"><textPath href="#arcStakeTop" startOffset="50%" text-anchor="middle">STAKEHOLDER ENGAGEMENT</textPath></text>
  <text class="stakeholder"><textPath href="#arcStakeRight" startOffset="50%" text-anchor="middle">STAKEHOLDER ENGAGEMENT</textPath></text>
  <text class="stakeholder"><textPath href="#arcStakeLeft" startOffset="50%" text-anchor="middle">STAKEHOLDER ENGAGEMENT</textPath></text>

  <!-- Blue cycle -->
  <g class="cycle-arrows" fill="none" stroke="var(--arrow-blue)" stroke-width="38">
    <path d="M626.3,403.8 A112 112 0 0 1 797.2,388.8" marker-end="url(#blueHead)"/>
    <path d="M819.5,420.7 A112 112 0 0 1 747,576.2" marker-end="url(#blueHead)"/>
    <path d="M708.2,579.6 A112 112 0 0 1 609.8,439" marker-end="url(#blueHead)"/>
  </g>
  <g class="cycle-dashes" fill="none" stroke="#fff" stroke-width="1.2" stroke-dasharray="5 4">
    <circle cx="718" cy="468" r="128"/>
    <circle cx="718" cy="468" r="96"/>
  </g>
  <text class="flow-label"><textPath href="#arcVision" startOffset="50%" text-anchor="middle">SHARED VISION</textPath></text>
  <text class="flow-label"><textPath href="#arcCoordination" startOffset="50%" text-anchor="middle">COORDINATION</textPath></text>
  <text class="flow-label"><textPath href="#arcDecision" startOffset="50%" text-anchor="middle">DECISION SUPPORT</textPath></text>

  <g class="core">
    <circle cx="718" cy="468" r="90" fill="var(--rust)"/>
    <circle cx="718" cy="468" r="76" fill="url(#coreFill)"/>
    <text class="core-label" text-anchor="middle">
      <tspan x="718" y="444">MARINE</tspan>
      <tspan x="718" y="476">SPATIAL</tspan>
      <tspan x="718" y="508">PLANNING</tspan>
    </text>
  </g>

  <!-- Adaptive management loop -->
  <g class="adaptive-loop" fill="none" stroke="var(--white)" stroke-width="14" stroke-linecap="round">
    <path d="M1135,325 Q1080,300 1030,335" marker-end="url(#whiteHead)"/>
    <path d="M1020,410 Q1075,440 1125,420" marker-end="url(#whiteHead)"/>
  </g>
  <text class="cycle-label" dy="5"><textPath href="#arcAdaptive" startOffset="50%" text-anchor="middle">ADAPTIVE</textPath></text>
  <text class="cycle-label" dy="5"><textPath href="#arcManagement" startOffset="50%" text-anchor="middle">MANAGEMENT</textPath></text>

  <!-- Map to benefits arrow -->
  <path d="M1352,482 Q1395,560 1335,612" fill="none" stroke="var(--white)" stroke-width="9" stroke-linecap="round" marker-end="url(#whiteHead)"/>

  <!-- National benefits -->
  <text class="benefits-title"><textPath href="#arcBenefits" startOffset="50%" text-anchor="middle">NATIONAL BENEFITS</textPath></text>
  <g class="benefits-venn">
    <circle cx="1213" cy="661" r="100" fill="var(--rust)"/>
    <circle cx="1130" cy="773" r="100" fill="var(--moss)"/>
    <circle cx="1295" cy="770" r="100" fill="var(--grey)"/>
    <circle cx="1130" cy="773" r="100" fill="var(--arrow-blue)" clip-path="url(#clipEcon)"/>
    <circle cx="1295" cy="770" r="100" fill="var(--arrow-blue)" clip-path="url(#clipEcon)"/>
    <circle cx="1295" cy="770" r="100" fill="var(--arrow-blue)" clip-path="url(#clipSocial)"/>
    <g fill="none" stroke="var(--ink)" stroke-width="0.8" stroke-dasharray="4 3" opacity="0.6">
      <circle cx="1213" cy="661" r="88"/>
      <circle cx="1130" cy="773" r="88"/>
      <circle cx="1295" cy="770" r="88"/>
    </g>
    <text class="venn-label" text-anchor="middle"><tspan x="1213" y="644">ECONOMIC</tspan><tspan x="1213" y="660">VALUE</tspan></text>
    <text class="venn-label" text-anchor="middle"><tspan x="1130" y="772">SOCIAL</tspan><tspan x="1130" y="788">DEVELOPMENT</tspan></text>
    <text class="venn-label" text-anchor="middle"><tspan x="1301" y="772">ENVIRONMENTAL</tspan><tspan x="1301" y="788">SUSTAINABILITY</tspan></text>
  </g>
</svg>
</body>
</html>
```